Vosk and Telby Website

Vosk & Telby Website

The purpose of the Vosk & Telby website has 2 purposes; number 1 is to SALE the most “Rugged and Reliable products with the most versatile innovation possible. Number 2 to attract and assist territory sales manager across the United States with an easy flow website and customer sales support in the background.

Our Website Vision

This Website should be very modern and professional with a easy flow, we will use the following platform and plug-ins built with then website builder Divi Word press with Woo commerce with a sales professional CRM ( submit the plug-in of your choice for review before adding to programming) in the backend. We will provide information to the look we are looking for. All background images will be Black and White. We will provide professional images of our products that have been trimmed out and saved with a transparent background so that they can be added to a custom designed background or black and white image that will enhance the product. I want all the special tools provided in the Divi Family of tools used to give this website the WOW FACTOR. As of Now or site will be hosted on Plume Vault

Header design should have a Center VT Logo provided with a Hamburger Menu on the left and on the right a Search Glass Icon a Person Icon for login and register and Sales Cart Icon this could in the only Page that is Full Page Black and White image that can be blurred or ghosted back as we want the main page to be a line of 6 to 8 different Carts and Dollies to represent our products in color. Designer can take the images of our product and color correct Photoshop or whatever is needed to make it look its best. That is the landing or main image. The home page will be a slider of up to five images with 4 major messages to our customer or reasons to do business with Vosk & Telby. I will download 2 image to give you a idea of direction.

Slider Messages: Price Match Guarantee
Industry Best Warranty 5 Years on Frame 3 Years on Casters
Customize to fit your Surface and Application
Designed, Engineered and Manufactured Proudly in the U.S.A.

Categories/ Products Page
Carts
Dollies
Casters
Used Equipment

Categories Page

Products Page
Ratings with stars and comments
WooCommerce Composite products

Customization Page

Career Page

Contact page

Policy Page

Terms and Conditions Page

LOOK AT ZELMIRAB7BAY.COM WEBSITE MUST BE BETTER

Target Market(s)

We are a manufacturer of the worlds most rugged and reliable Industrial carts, dollies, hand trucks and casters. we will be selling to all types of industry's from distributors warehouse hospitals

Industry/Entity Type

Light Industrial

Coding

Coded - Design and coding required

Number of Pages Required

5+ page

Colors
ec1f27

Requirements
Must have
• Monochrome with Products colored and buttons and logo color codes in logo are Red # AF002A and Gray #5B5C5E
• Divi we own a lifetime license
• WordPress
• Woocommerce
• woocommerce composite products
• WP forms
• CRM
• Welder image is meant to be used Customization Page
Nice to have
• CRM for our 100 plus reps

```html
<!DOCTYPE html>
<html lang="en">
<head>
<meta charset="utf-8">
<title>Vosk &amp; Telby — Rugged and Reliable Industrial Carts</title>
<link href="https://fonts.googleapis.com/css2?family=Exo+2:wght@400;500;600;700;800&family=Open+Sans:wght@400;600&display=swap" rel="stylesheet">
<style>
:root{
  --red:#c8001e;
  --red-deep:#a80020;
  --red-bright:#ec1f27;
  --gray:#5b5c5e;
  --ink:#1d1d1f;
  --text:#555658;
  --footer:#4a4a4c;
  --white:#ffffff;
  --silver:#b9babc;
  --teal:#237f9c;
  --navy:#163f78;
}
*{margin:0;padding:0;box-sizing:border-box}
html,body{width:1200px;height:3575px;overflow:hidden}
body{position:relative;font-family:"Open Sans",sans-serif;color:var(--text);background:var(--white)}
.section{position:absolute;left:0;width:1200px;overflow:hidden}
.abs{position:absolute}
.heading{font-family:"Exo 2",sans-serif;font-weight:600;color:var(--ink);text-transform:uppercase;letter-spacing:.5px}
.heading .accent{color:var(--red)}
.btn{position:absolute;display:flex;align-items:center;justify-content:center;font-family:"Exo 2",sans-serif;font-weight:700;font-size:16px;text-transform:uppercase;border-radius:26px}
.btn-solid{background:var(--red);color:var(--white)}
.btn-outline{border:2px solid var(--red);color:var(--red);background:var(--white)}
.brand{display:flex;align-items:center;gap:10px;font-family:"Exo 2",sans-serif;font-weight:800;color:var(--white);letter-spacing:1px}
.brand-mark{background:var(--red);border-radius:4px}
.photo{border-radius:6px;box-shadow:0 10px 24px rgba(0,0,0,.18)}

/* hero */
.hero{top:0;height:760px;background:linear-gradient(180deg,#2e2e30 0%,#444446 45%,#646466 80%,#7e7e80 100%)}
.utility{position:absolute;top:8px;right:80px;display:flex;gap:26px;align-items:center;font-family:"Exo 2",sans-serif;font-size:13px;color:var(--white)}
.nav{position:absolute;top:62px;left:540px;display:flex;gap:32px;font-family:"Exo 2",sans-serif;font-weight:500;font-size:16px;color:var(--white)}
.hero-kicker{left:137px;top:288px;font-family:"Exo 2",sans-serif;font-size:26px;color:var(--white);letter-spacing:.5px}
.hero-title{left:137px;top:322px;font-family:"Exo 2",sans-serif;font-weight:800;font-size:42px;line-height:50px;color:var(--white)}
.hero-shot{left:650px;top:150px;width:360px;height:455px;background:linear-gradient(160deg,#e8202c 0%,#c4001d 55%,#8e0018 100%)}
.dots{left:550px;top:670px;display:flex;gap:6px;align-items:center}
.dot{width:9px;height:9px;border-radius:50%;background:#cfcfd1}
.dot.on{background:var(--white)}
.dot-arrow{width:20px;height:20px;border-radius:50%;background:var(--white);color:var(--ink);font-size:12px;display:flex;align-items:center;justify-content:center;font-weight:700}

/* about */
.about{top:760px;height:392px;background:var(--white)}
.about p{position:absolute;left:622px;width:490px;font-size:16px;line-height:27px}
.about-shot{left:146px;top:76px;width:420px;height:300px;background:linear-gradient(180deg,#48484a 0%,#2a2a2c 100%)}

/* featured */
.featured{top:1152px;height:732px;background:linear-gradient(180deg,#d9d9db 0%,#f0f0f1 55%,#ffffff 100%)}
.product{position:absolute;top:0;width:240px;text-align:center}
.product-shot{position:absolute;left:35px;top:205px;width:170px;height:290px}
.product-title{position:absolute;top:524px;width:240px;font-family:"Exo 2",sans-serif;font-weight:700;font-size:17px;color:var(--ink)}
.product-sub{position:absolute;top:548px;width:240px;font-size:15px;color:#333}
.product-price{position:absolute;top:573px;width:240px;font-family:"Exo 2",sans-serif;font-weight:600;font-size:23px;color:var(--ink)}
.product .btn{left:44px;top:614px;width:152px;height:42px;font-size:15px;font-weight:600}
.chev{position:absolute;width:30px;height:60px}

/* why */
.why{top:1884px;height:432px;background:radial-gradient(ellipse at 50% 60%,#3c3c3e 0%,#252527 70%)}
.why-card{position:absolute;top:172px;width:227px;height:212px;background:var(--white);text-align:center}
.why-icon{position:absolute;top:-50px;left:69px;width:90px;height:90px;border-radius:50%;background:var(--red);border:4px solid var(--white);box-shadow:0 0 0 1px #ddd;display:flex;align-items:center;justify-content:center}
.why-card h3{margin-top:72px;font-family:"Exo 2",sans-serif;font-weight:700;font-size:17px;color:var(--red-deep);text-transform:uppercase}
.why-card p{margin:8px auto 0;width:188px;font-size:13px;line-height:18px;color:#444}

/* testimonials */
.testimonials{top:2316px;height:500px;background:linear-gradient(90deg,#e5001e 0%,#c8001e 55%,#9c0020 100%)}
.quote-card{position:absolute;top:189px;width:383px;height:216px;background:var(--white);text-align:center}
.avatar{position:absolute;top:-44px;left:146px;width:90px;height:90px;border-radius:50%;background:linear-gradient(180deg,#c4c4c6,#8a8a8d);border:3px solid var(--red)}
.quote-card h4{margin-top:54px;font-family:"Exo 2",sans-serif;font-weight:700;font-size:17px;color:var(--ink)}
.quote-card .place{font-size:13px;color:#555}
.quote-card p{margin:12px auto 0;width:330px;font-size:14px;line-height:22px;color:#444}

/* find */
.find{top:2816px;height:367px;background:linear-gradient(90deg,#e0e0e1 0%,#f2f2f3 60%,#eeeeef 100%)}
.find p{position:absolute;left:545px;top:145px;width:580px;font-size:17px;line-height:27px;color:#333}

/* footer */
.footer{top:3183px;height:392px;background:var(--footer);color:#d8d8da}
.footer h5{position:absolute;top:65px;font-family:"Exo 2",sans-serif;font-weight:700;font-size:16px;color:var(--white);text-transform:uppercase}
.footer ul{position:absolute;top:97px;list-style:none;font-size:13.5px;line-height:22.6px}
.contact-line{position:absolute;left:158px;font-size:13.5px;line-height:20px}
.contact-line strong{display:block;font-weight:400;font-size:17px;color:var(--white)}
.social{position:absolute;top:98px;left:892px;display:flex;gap:7px}
.social span{width:33px;height:33px;border-radius:50%;border:2px solid #e8e8ea}
.pay{position:absolute;top:156px;left:895px;display:flex;gap:14px}
.pay span{width:35px;height:22px;border-radius:3px;background:#d9d9db}
.copy{position:absolute;top:318px;height:74px;line-height:74px;width:1200px;text-align:center;font-size:13px;color:#bdbdbf;border-top:1px solid #5c5c5e}
</style>
</head>
<body>

<!-- HERO -->
<section class="section hero">
  <div class="abs" role="img" aria-label="Black and white photograph of an empty industrial warehouse interior" style="inset:0;background:linear-gradient(180deg,rgba(20,20,22,.3),rgba(120,120,122,.1))"></div>

  <div class="utility">
    <svg width="16" height="16" viewBox="0 0 16 16"><circle cx="6.5" cy="6.5" r="5" fill="none" stroke="#fff" stroke-width="2"/><line x1="10.5" y1="10.5" x2="15" y2="15" stroke="#fff" stroke-width="2"/></svg>
    <span>MY ACCOUNT</span><span>REGISTER</span><span>LOGIN</span>
  </div>

  <div class="brand abs" style="left:132px;top:48px;font-size:34px">
    <span class="brand-mark" style="width:40px;height:40px"></span>VOSK &amp; TELBY
  </div>

  <nav class="nav">
    <span>PRODUCTS</span><span>ABOUT</span><span>WHY US</span><span>PRODUCTS ▾</span><span>SHOP</span><span>CONTACT</span>
  </nav>

  <div class="abs hero-kicker">RUGGED AND RELIABLE</div>
  <h1 class="abs hero-title">INDUSTRIAL CARTS,<br>DOLLIES HAND TRUCKS</h1>
  <div class="btn btn-solid" style="left:143px;top:434px;width:180px;height:52px;border-radius:0;font-size:18px">SHOP NOW</div>

  <div class="abs photo hero-shot" role="img" aria-label="Red industrial utility cart with tall handle and casters"></div>

  <div class="abs dots">
    <span class="dot-arrow">‹</span><span class="dot on"></span><span class="dot"></span><span class="dot"></span><span class="dot"></span><span class="dot-arrow">›</span>
  </div>

  <svg class="abs" style="left:0;top:660px" width="1200" height="100" viewBox="0 660 1200 100">
    <polygon points="700,710 1200,672 1200,700" fill="var(--red)"/>
    <polygon points="760,713 1200,700 1200,748" fill="#bfbfc1"/>
    <polygon points="0,757 700,710 760,713 1200,748 1200,760 0,760" fill="#fff"/>
  </svg>
</section>

<!-- ABOUT -->
<section class="section about">
  <div class="abs photo about-shot" role="img" aria-label="Dark three-shelf steel utility cart on casters"></div>
  <h2 class="abs heading" style="left:622px;top:68px;font-size:30px">ABOUT <span class="accent">VOSK &amp; TELBY</span></h2>
  <p style="top:120px;font-size:16.5px;color:#444">Fusce tellus Sed metus augue convallis et vehicula ut pulvinar eu ante Integer orci tellus tristique vitae</p>
  <p style="top:205px;font-size:15px;line-height:27px">Aonsequat nec porta vel lectus Nulla sit amet diam aliquam enim Proin dui lectus cursus eu mattis laoreet viverra sit amet quam Curabitur vel dolor ultrices ipsum dictum tristique Pr</p>
  <div class="btn btn-solid" style="left:620px;top:311px;width:179px;height:46px">LEARN MORE</div>
</section>

<!-- FEATURED -->
<section class="section featured">
  <div class="abs" role="img" aria-label="Black and white photograph of a warehouse roof structure" style="inset:0;background:linear-gradient(180deg,rgba(190,190,192,.45),rgba(255,255,255,0) 80%)"></div>
  <svg class="abs" style="left:0;top:0" width="1200" height="110" viewBox="0 0 1200 110">
    <polygon points="0,0 1200,0 380,72 0,24" fill="#fff"/>
    <polygon points="0,24 385,70 0,104" fill="var(--red)"/>
    <polygon points="0,58 250,84 0,104" fill="var(--red-bright)"/>
  </svg>
  <h2 class="abs heading" style="left:0;width:1200px;text-align:center;top:104px;font-size:30px">FEATURED <span class="accent">PRODUCTS</span></h2>

  <svg class="chev" style="left:66px;top:348px" viewBox="0 0 30 60"><polyline points="28,2 2,30 28,58" fill="none" stroke="#333" stroke-width="2"/></svg>
  <svg class="chev" style="left:1120px;top:348px" viewBox="0 0 30 60"><polyline points="2,2 28,30 2,58" fill="none" stroke="#333" stroke-width="2"/></svg>

  <div class="product" style="left:91px">
    <div class="product-shot photo" role="img" aria-label="Silver aluminium hand truck" style="background:linear-gradient(160deg,#d6d7d9,var(--silver) 60%,#8f9092)"></div>
    <div class="product-title">PRODUCT TITLE</div>
    <div class="product-sub">Fusce tellus Sed metus</div>
    <div class="product-price">$150.99</div>
    <div class="btn btn-outline">ADD TO CART</div>
  </div>
  <div class="product" style="left:346px">
    <div class="product-shot photo" role="img" aria-label="Teal steel hand truck" style="background:linear-gradient(160deg,#3a97b4,var(--teal) 60%,#185f77)"></div>
    <div class="product-title">PRODUCT TITLE</div>
    <div class="product-sub">Fusce tellus Sed metus</div>
    <div class="product-price">$150.99</div>
    <div class="btn btn-outline">ADD TO CART</div>
  </div>
  <div class="product" style="left:601px">
    <div class="product-shot photo" role="img" aria-label="Teal convertible hand truck with forks" style="background:linear-gradient(160deg,#3a97b4,var(--teal) 60%,#185f77)"></div>
    <div class="product-title">PRODUCT TITLE</div>
    <div class="product-sub">Fusce tellus Sed metus</div>
    <div class="product-price">$150.99</div>
    <div class="btn btn-outline">ADD TO CART</div>
  </div>
  <div class="product" style="left:856px">
    <div class="product-shot photo" role="img" aria-label="Navy blue platform cart" style="background:linear-gradient(160deg,#2b5a98,var(--navy) 60%,#0d2a52)"></div>
    <div class="product-title">PRODUCT TITLE</div>
    <div class="product-sub">Fusce tellus Sed metus</div>
    <div class="product-price">$150.99</div>
    <div class="btn btn-outline">ADD TO CART</div>
  </div>
</section>

<!-- WHY -->
<section class="section why">
  <div class="abs" role="img" aria-label="Black and white photograph of welding sparks" style="inset:0;background:radial-gradient(ellipse at 80% 40%,rgba(120,120,122,.25),rgba(0,0,0,0) 60%)"></div>
  <h2 class="abs heading" style="left:0;width:1200px;text-align:center;top:55px;font-size:29px;color:#fff">WHY CHOOSE VOSK &amp; TELBY</h2>

  <div class="why-card" style="left:118px">
    <div class="why-icon"><svg width="44" height="44" viewBox="0 0 44 44"><circle cx="22" cy="22" r="16" fill="none" stroke="#fff" stroke-width="2.5"/><text x="22" y="30" text-anchor="middle" font-family="Open Sans,sans-serif" font-size="22" font-weight="600" fill="#fff">$</text></svg></div>
    <h3>BEST PRICES</h3>
    <p>Fusce tellus Sed metus augue convallis et vehicula ut pulvinar eu ante Integer orci tellus tristique vitae</p>
  </div>
  <div class="why-card" style="left:361px">
    <div class="why-icon"><svg width="48" height="48" viewBox="0 0 48 48"><circle cx="24" cy="24" r="20" fill="none" stroke="#fff" stroke-width="2.5"/><polyline points="15,24 22,31 34,17" fill="none" stroke="#fff" stroke-width="2.5"/></svg></div>
    <h3>HIGHEST QUALITY</h3>
    <p>Fusce tellus Sed metus augue convallis et vehicula ut pulvinar eu ante Integer orci tellus tristique vitae</p>
  </div>
  <div class="why-card" style="left:604px">
    <div class="why-icon"><svg width="44" height="44" viewBox="0 0 44 44"><polygon points="22,5 27,17 40,17 29.5,25 33.5,38 22,30 10.5,38 14.5,25 4,17 17,17" fill="none" stroke="#fff" stroke-width="2.5" stroke-linejoin="round"/></svg></div>
    <h3>INDUSTRY LEADERS</h3>
    <p>Fusce tellus Sed metus augue convallis et vehicula ut pulvinar eu ante Integer orci tellus tristique vitae</p>
  </div>
  <div class="why-card" style="left:847px">
    <div class="why-icon"><svg width="44" height="44" viewBox="0 0 44 44"><path d="M9 26 V20 a13 13 0 0 1 26 0 V26" fill="none" stroke="#fff" stroke-width="2.5"/><rect x="6" y="23" width="7" height="11" rx="2" fill="none" stroke="#fff" stroke-width="2.5"/><rect x="31" y="23" width="7" height="11" rx="2" fill="none" stroke="#fff" stroke-width="2.5"/><path d="M34 34 q0 5 -8 5" fill="none" stroke="#fff" stroke-width="2.5"/></svg></div>
    <h3>CUSTOMER SERVICE</h3>
    <p>Fusce tellus Sed metus augue convallis et vehicula ut pulvinar eu ante Integer orci tellus tristique vitae</p>
  </div>
</section>

<!-- TESTIMONIALS -->
<section class="section testimonials">
  <svg class="abs" style="left:0;top:0" width="1200" height="500" viewBox="0 0 1200 500">
    <polygon points="830,20 1200,6 1200,64" fill="#c4c4c6"/>
    <polygon points="0,452 620,500 0,500" fill="#2e2e30"/>
    <polygon points="620,500 1200,470 1200,500" fill="#2e2e30"/>
  </svg>
  <h2 class="abs heading" style="left:0;width:1200px;text-align:center;top:104px;font-size:29px;color:#fff">TESTIMONIALS</h2>

  <svg class="chev" style="left:126px;top:255px" viewBox="0 0 30 60"><polyline points="28,4 4,30 28,56" fill="none" stroke="#fff" stroke-width="2"/></svg>
  <svg class="chev" style="left:1046px;top:255px" viewBox="0 0 30 60"><polyline points="2,4 26,30 2,56" fill="none" stroke="#fff" stroke-width="2"/></svg>

  <div class="quote-card" style="left:192px">
    <div class="avatar" role="img" aria-label="Portrait photo of customer"></div>
    <h4>Dara Quillen</h4>
    <div class="place">City Location</div>
    <p>Fusce tellus Sed metus augue convallis et vehicula ut pulvinar eu ante Integer orci tellus tristique vitae consequat nec porta vel lectus Nulla sit amet enim Proin dui lectus</p>
  </div>
  <div class="quote-card" style="left:624px">
    <div class="avatar" role="img" aria-label="Portrait photo of customer"></div>
    <h4>Tomas Revik</h4>
    <div class="place">City Location</div>
    <p>Fusce tellus Sed metus augue convallis et vehicula ut pulvinar eu ante Integer orci tellus tristique vitae consequat nec porta vel lectus Nulla sit amet enim Proin dui lectus</p>
  </div>
</section>

<!-- FIND -->
<section class="section find">
  <div class="abs" style="left:-40px;top:-50px;width:520px;height:470px;border-radius:50%;background:#d2d2d4"></div>
  <div class="abs" style="left:-20px;top:-30px;width:440px;height:430px;border-radius:50%;background:#bdbdbf"></div>
  <div class="abs" role="img" aria-label="Black and white warehouse photograph in a circular frame" style="left:56px;top:36px;width:290px;height:290px;border-radius:50%;background:radial-gradient(circle at 50% 40%,#f4f4f5,#b4b4b6)"></div>
  <div class="abs photo" role="img" aria-label="Red industrial utility cart with tall handle" style="left:95px;top:20px;width:210px;height:300px;background:linear-gradient(160deg,#e8202c 0%,#c4001d 55%,#8e0018 100%)"></div>
  <h2 class="abs heading" style="left:544px;top:88px;font-size:29px;color:#3a3a3c">FIND YOUR CARTS &amp; DOLLIES</h2>
  <p>Lorem ipsum dolor sit amet, consectetur adipiscing elit, sed do eiusmod tempor incididunt ut labore et dolore magna aliqua.</p>
  <div class="btn btn-solid" style="left:542px;top:219px;width:180px;height:46px">FIND NOW</div>
  <div class="btn" style="left:731px;top:219px;width:179px;height:46px;border:2px solid #4a4a4c;color:#3a3a3c">CONTACT US</div>
</section>

<!-- FOOTER -->
<footer class="section footer">
  <div class="brand abs" style="left:125px;top:68px;font-size:24px">
    <span class="brand-mark" style="width:30px;height:30px"></span>VOSK &amp; TELBY
  </div>

  <svg class="abs" style="left:126px;top:140px" width="22" height="22" viewBox="0 0 22 22"><path d="M5 2 L9 6 L7 9 Q9 13 13 15 L16 13 L20 17 L17 20 Q9 20 2 5 Z" fill="none" stroke="#ddd" stroke-width="1.5"/></svg>
  <div class="contact-line" style="top:130px">Call Us Now<strong>(685) 555 0172</strong></div>
  <svg class="abs" style="left:126px;top:203px" width="24" height="18" viewBox="0 0 24 18"><rect x="1" y="1" width="22" height="16" fill="none" stroke="#ddd" stroke-width="1.5"/><polyline points="1,1 12,10 23,1" fill="none" stroke="#ddd" stroke-width="1.5"/></svg>
  <div class="contact-line" style="top:190px">Email Us<strong style="font-size:15px">hello@vosktelby.example</strong></div>

  <h5 style="left:415px">Company</h5>
  <ul style="left:416px"><li>About Us</li><li>Terms &amp; Conditions</li><li>Return Policy</li><li>Best Price Guarantee</li><li>Shipping Information</li><li>Privacy Policy</li></ul>

  <h5 style="left:606px">Resources</h5>
  <ul style="left:606px"><li>Pellentesque</li><li>Faucibus Ut</li><li>Accumsan ultri</li><li>Enim vestibulum</li><li>Non fermentum</li><li>Aec hend</li></ul>

  <h5 style="left:763px">Help</h5>
  <ul style="left:765px"><li>Contact Us</li><li>Register</li><li>Login</li><li>Order History</li><li>Site Map</li><li>Search</li></ul>

  <h5 style="left:892px">Get in Touch</h5>
  <div class="social"><span></span><span></span><span></span><span></span></div>
  <div class="pay"><span></span><span></span><span></span><span></span></div>

  <div class="copy">Copyright © 2019 All right reserved</div>
</footer>

</body>
</html>
```